Existing Website Requiring new Pages

I have an existing word press website that was built using elementor.
Website: www.tallowmerecare.com.au
I require the Vacancies page (https://www.tallowmerecare.com.au/vacancies/) to be modified to display our new properties along with minor tweaks to how the information is presented.
The vacancies to be displayed are the exactly the same as those that are located on the homepage of QDA website (https://qda.org.au/)
The new pages that link off the Vacancies tab will require custom design.
There are roughly 8 pages/properties to be incorporated. i wish for the design to be very similar to that displayed in the following link; https://www.zomplex.com.au/vacancies/merrylands
Along with this the back end has not been updated for the last 3 years so it also requires some maintenance.
Website is in the disability industry and the custom pages will display information relative to Property Vacancies.
I have attached a ZIP file with some design guides, the information for each of the properties (which will need to be modified to show our business name Tallowmere Healthcare) and the example of how it is to look based off the Zomplex website.
If you guys have any suggestions or ideas on how to make this more presentable or possible i'm open to your ideas.
People looking for SDA properties custom built for people with a disability
Disability
Coded - Design and coding required
5+ page

```html
<!DOCTYPE html>
<html lang="en">
<head>
<meta charset="utf-8">
<title>Vacancies – Tallowmere Healthcare</title>
<link href="https://fonts.googleapis.com/css2?family=Montserrat:wght@400;500;600;700&display=swap" rel="stylesheet">
<style>
:root{
  --orange:#fbb25c;
  --pink:#e1479d;
  --ink:#222;
  --muted:#555;
  --soft:#f8f5ef;
  --line:#e5e5e5;
  --footer-link:#8a8a8a;
  --blue:#1f8fd6;
  --dark:#232323;
}
*{box-sizing:border-box;margin:0;padding:0}
html,body{width:1200px;height:3363px;overflow:hidden;background:#fff;font-family:'Montserrat',sans-serif;color:var(--ink)}
.page{position:relative;width:1200px;height:3363px}
.site-header{position:absolute;top:0;left:0;width:1200px;height:142px;background:#fff}
.brand{position:absolute;left:64px;top:52px;display:flex;align-items:center;gap:10px;font-size:17px;font-weight:600;color:var(--pink)}
.brand .dot{width:22px;height:22px;border-radius:50%;background:var(--pink)}
.main-nav{position:absolute;top:64px;left:564px;display:flex;font-size:11.5px;font-weight:700;letter-spacing:.8px;color:#444}
.main-nav a{position:absolute;white-space:nowrap;color:inherit;text-decoration:none}
.main-nav .current{color:var(--orange)}
.hero{position:absolute;top:142px;left:0;width:1200px;height:520px;overflow:hidden}
.hero-photo{position:absolute;inset:0;background:linear-gradient(120deg,#8b6a5a 0%,#a89686 35%,#6e6a66 60%,#3d3b3a 100%)}
.hero-shape{position:absolute;inset:0}
.hero-title{position:absolute;left:57px;top:228px;font-size:50px;font-weight:700;color:#fff;text-shadow:0 2px 6px rgba(0,0,0,.15)}
.search-card{position:absolute;left:112px;top:529px;width:976px;height:600px;background:var(--soft);border-radius:22px;box-shadow:0 6px 18px rgba(0,0,0,.08)}
.filter-box{position:absolute;left:32px;top:32px;width:911px;height:114px;background:#fff;border-radius:14px}
.filter{position:absolute;top:26px;width:251px}
.filter label{display:block;font-size:13px;font-weight:500;color:#333;margin-bottom:10px}
.select{height:38px;border:1px solid #ddd;border-radius:3px;font-size:13px;color:#999;padding:0 16px;display:flex;align-items:center;justify-content:space-between}
.select svg{width:10px;height:10px}
.go-btn{position:absolute;left:817px;top:50px;width:69px;height:38px;background:var(--pink);color:#fff;font-size:14px;font-weight:600;display:flex;align-items:center;justify-content:center;border-radius:2px}
.eyebrow{position:absolute;left:32px;top:163px;font-size:13px;color:#333}
.section-heading{position:absolute;left:32px;top:186px;font-size:22px;font-weight:500}
.map{position:absolute;left:32px;top:237px;width:911px;height:331px;background:linear-gradient(90deg,#a9c8b4 0%,#d4e6d6 30%,#e8eeea 55%,#f0f0ee 100%);border-radius:0 0 18px 18px}
.map-zoom{position:absolute;right:16px;bottom:20px;width:34px;height:78px;background:#fff;border-radius:3px;box-shadow:0 1px 4px rgba(0,0,0,.25);font-size:24px;font-weight:500;color:#333;text-align:center;line-height:38px}
.list-heading{position:absolute;left:112px;top:1205px;font-size:23px;font-weight:500}
.cards{position:absolute;left:115px;top:1276px;display:grid;grid-template-columns:repeat(3,313px);column-gap:18px;row-gap:34px}
.card{position:relative;width:313px;height:517px;background:#fff;box-shadow:0 2px 12px rgba(0,0,0,.08)}
.card-photo{position:relative;width:313px;height:313px}
.p1{background:linear-gradient(180deg,#c9d4dc,#8e8a78 60%,#6b6b62)}
.p2{background:linear-gradient(180deg,#c8d0d8,#7d6f66 55%,#8e8f88)}
.p3{background:linear-gradient(180deg,#d9dcdf,#7b5e50 50%,#90877c)}
.p4{background:linear-gradient(180deg,#5f8fd0,#c9d9ea 30%,#4a4d52 55%,#a9a9a6)}
.p5{background:linear-gradient(180deg,#9bb3d4,#6a5d55 50%,#7aa05c)}
.p6{background:linear-gradient(180deg,#2f7ad9,#6b6c70 45%,#6f7f58)}
.p7{background:linear-gradient(180deg,#f2f2f2,#dcdcdc 40%,#7fb3a0 60%,#b58d6a)}
.p8{background:linear-gradient(180deg,#a7c3e0,#a36a4f 40%,#8a7a6e)}
.p9{background:linear-gradient(180deg,#b9c1c9,#55575b 50%,#3f4245)}
.tags{position:absolute;top:14px;left:10px;right:10px;display:flex;gap:6px}
.tag{height:22px;padding:0 11px;border-radius:11px;background:rgba(40,40,40,.75);color:#fff;font-size:10.5px;font-weight:700;display:flex;align-items:center;letter-spacing:.2px}
.tag.featured{background:var(--orange)}
.tag.push{margin-left:auto}
.dots{position:absolute;bottom:14px;left:0;right:0;display:flex;justify-content:center;gap:5px}
.dots i{width:6px;height:6px;border-radius:50%;background:rgba(255,255,255,.7)}
.dots i:first-child{background:#222}
.card-body{position:absolute;left:22px;top:333px;right:14px}
.card-title{font-size:19px;font-weight:600;white-space:nowrap;overflow:hidden;text-overflow:ellipsis}
.card-location{font-size:13px;color:var(--muted);margin-top:7px}
.card-features{font-size:13px;color:var(--muted);margin-top:16px;line-height:1.3}
.details-btn{position:absolute;left:22px;top:457px;width:89px;height:38px;background:var(--pink);color:#fff;font-size:15px;font-weight:600;display:flex;align-items:center;justify-content:center;border-radius:2px}
.site-footer{position:absolute;left:0;top:2966px;width:1200px;height:324px;background:#fff;border-top:1px solid #f0f0f0}
.footer-brand{position:absolute;left:78px;top:85px;display:flex;align-items:center;gap:10px;font-size:18px;font-weight:600;color:var(--pink)}
.footer-brand .dot{width:24px;height:24px;border-radius:50%;background:var(--pink)}
.contact{position:absolute;left:72px;top:230px;font-size:13.5px;color:var(--pink);line-height:24px}
.contact li{list-style:none;display:flex;align-items:center;gap:9px}
.contact svg{width:14px;height:14px}
.social{position:absolute;left:514px;top:74px;display:flex;flex-direction:column;gap:10px}
.social i{display:block;width:34px;height:34px;border-radius:50%;background:#1f3c6e}
.social i:first-child{background:#6b2c82}
.footer-col{position:absolute;top:66px;width:243px}
.footer-col h4{font-size:14.5px;font-weight:500;letter-spacing:.5px;border-left:3px solid var(--blue);padding-left:14px;line-height:16px;margin-bottom:16px}
.footer-col a{display:block;font-size:13.5px;color:var(--footer-link);text-decoration:none;border-bottom:1px solid var(--line);padding:8px 0;line-height:22px}
.copyright{position:absolute;left:0;top:3290px;width:1200px;height:73px;background:var(--dark);color:#bbb;font-size:11px;display:flex;align-items:center;justify-content:center}
</style>
</head>
<body>
<div class="page">
  <header class="site-header">
    <div class="brand"><span class="dot"></span>Tallowmere Healthcare</div>
    <nav class="main-nav">
      <a style="left:0">HOME</a>
      <a style="left:68px">ABOUT US</a>
      <a class="current" style="left:163px">WHAT WE DO ⌄</a>
      <a style="left:300px">REFERRALS</a>
      <a style="left:405px">FEEDBACK</a>
      <a style="left:504px">CONTACT US</a>
    </nav>
  </header>

  <section class="hero">
    <div class="hero-photo" role="img" aria-label="Woman in a wheelchair working on a laptop at a kitchen table"></div>
    <svg class="hero-shape" width="1200" height="520" viewBox="0 0 1200 520">
      <polygon points="0,0 352,0 490,387 112,387 112,520 0,520" fill="var(--orange)"/>
    </svg>
    <h1 class="hero-title">Vacancies</h1>
  </section>

  <section class="search-card">
    <div class="filter-box">
      <div class="filter" style="left:24px"><label>Current or Future</label><div class="select">Both<svg viewBox="0 0 10 10"><path d="M1 3l4 4 4-4" fill="none" stroke="#666" stroke-width="1.3"/></svg></div></div>
      <div class="filter" style="left:288px"><label>Design Category</label><div class="select">All Categories<svg viewBox="0 0 10 10"><path d="M1 3l4 4 4-4" fill="none" stroke="#666" stroke-width="1.3"/></svg></div></div>
      <div class="filter" style="left:552px"><label>Location</label><div class="select">All Suburbs<svg viewBox="0 0 10 10"><path d="M1 3l4 4 4-4" fill="none" stroke="#666" stroke-width="1.3"/></svg></div></div>
      <div class="go-btn">Go</div>
    </div>
    <p class="eyebrow">Properties</p>
    <h2 class="section-heading">View our SDA vacancies and homes being built</h2>
    <div class="map" role="img" aria-label="Map of western Sydney showing property locations">
      <div class="map-zoom">+<br>−</div>
    </div>
  </section>

  <h2 class="list-heading">Properties List View</h2>

  <main class="cards">
    <article class="card"><div class="card-photo p1" role="img" aria-label="Two-storey brick home in Greystanes"><div class="tags"><span class="tag featured">FEATURED</span><span class="tag push">ALMOST FULL</span><span class="tag">APPLY</span></div><div class="dots"><i></i><i></i><i></i><i></i><i></i></div></div><div class="card-body"><h3 class="card-title">SDA IN Greystanes</h3><p class="card-location">Greystanes</p><p class="card-features">Fully Accessible, High Physical Support</p></div><a class="details-btn">Details</a></article>
    <article class="card"><div class="card-photo p2" role="img" aria-label="Brick townhouse with open garage in Jordan Springs"><div class="tags"><span class="tag featured">FEATURED</span><span class="tag push">ALMOST FULL</span><span class="tag">APPLY</span></div><div class="dots"><i></i><i></i><i></i><i></i><i></i></div></div><div class="card-body"><h3 class="card-title">SDA in Jordan Springs</h3><p class="card-location">Jordan Springs</p><p class="card-features">Fully Accessible, Improved Liveability</p></div><a class="details-btn">Details</a></article>
    <article class="card"><div class="card-photo p3" role="img" aria-label="Brick home entrance with security door in Werrington"><div class="tags"><span class="tag featured">FEATURED</span><span class="tag push">ALMOST FULL</span><span class="tag">APPLY</span></div><div class="dots"><i></i><i></i><i></i><i></i><i></i></div></div><div class="card-body"><h3 class="card-title">SDA in Werrington</h3><p class="card-location">Werrington</p><p class="card-features">Fully Accessible, Improved Liveability</p></div><a class="details-btn">Details</a></article>

    <article class="card"><div class="card-photo p4" role="img" aria-label="Single-storey villas with white doors in Wentworthville"><div class="tags"><span class="tag featured">FEATURED</span><span class="tag push">ALMOST FULL</span><span class="tag">APPLY</span></div><div class="dots"><i></i><i></i><i></i><i></i><i></i></div></div><div class="card-body"><h3 class="card-title">SDA villas in Wentworthville</h3><p class="card-location">Wentworthville</p><p class="card-features">Fully Accessible, High Physical Support, Improved Liveability</p></div><a class="details-btn">Details</a></article>
    <article class="card"><div class="card-photo p5" role="img" aria-label="Two-storey brick home with lawn in West Pennant Hills"><div class="tags"><span class="tag featured">FEATURED</span><span class="tag push">ALMOST FULL</span><span class="tag">APPLY</span></div><div class="dots"><i></i><i></i><i></i><i></i><i></i></div></div><div class="card-body"><h3 class="card-title">SDA in West Pennant Hills</h3><p class="card-location">West Pennant Hills</p><p class="card-features">High Physical Support</p></div><a class="details-btn">Details</a></article>
    <article class="card"><div class="card-photo p6" role="img" aria-label="Dark brick home under blue sky in Guildford West"><div class="tags"><span class="tag featured">FEATURED</span><span class="tag push">ALMOST FULL</span><span class="tag">APPLY</span></div><div class="dots"><i></i><i></i><i></i><i></i><i></i></div></div><div class="card-body"><h3 class="card-title">SDA in Guildford West</h3><p class="card-location">Guildford West</p><p class="card-features">Fully Accessible, High Physical Support</p></div><a class="details-btn">Details</a></article>

    <article class="card"><div class="card-photo p7" role="img" aria-label="New kitchen with green tiles and white cabinets in Austral"><div class="tags"><span class="tag">REGISTER YOUR INTEREST TODAY</span><span class="tag push">APPLY</span></div><div class="dots"><i></i><i></i><i></i><i></i><i></i></div></div><div class="card-body"><h3 class="card-title">SDA in Austral</h3><p class="card-location">Austral</p><p class="card-features">Fully Accessible, High Physical Support, Robust</p></div><a class="details-btn">Details</a></article>
    <article class="card"><div class="card-photo p8" role="img" aria-label="Brick townhouses along a street in Merrylands"><div class="tags"><span class="tag push">AVAILABLE NOW</span><span class="tag">APPLY</span></div><div class="dots"><i></i><i></i><i></i><i></i><i></i></div></div><div class="card-body"><h3 class="card-title">SDA in Merrylands</h3><p class="card-location">SDA in Merrylands</p><p class="card-features">Fully Accessible, High Physical Support</p></div><a class="details-btn">Details</a></article>
    <article class="card"><div class="card-photo p9" role="img" aria-label="Modern dark single-storey home in Blacktown"><div class="tags"><span class="tag push">EXPRESSION OF INTEREST</span><span class="tag">APPLY</span></div><div class="dots"><i></i><i></i><i></i><i></i><i></i></div></div><div class="card-body"><h3 class="card-title">SDA in Blacktown – 1 bedroom</h3><p class="card-location">Blacktown</p><p class="card-features">High Physical Support</p></div><a class="details-btn">Details</a></article>
  </main>

  <footer class="site-footer">
    <div class="footer-brand"><span class="dot"></span>Tallowmere Healthcare</div>
    <ul class="contact">
      <li><svg viewBox="0 0 14 14"><rect x="1" y="3" width="12" height="8" fill="none" stroke="currentColor" stroke-width="1.3"/><path d="M1 3l6 5 6-5" fill="none" stroke="currentColor" stroke-width="1.3"/></svg>Email: info@tallowmerecare.com.au</li>
      <li><svg viewBox="0 0 14 14"><path d="M3 1l3 3-2 2c1 2 2 3 4 4l2-2 3 3-2 2C6 13 1 8 1 3z" fill="currentColor"/></svg>Phone: +61 0491 570 156</li>
      <li><svg viewBox="0 0 14 14"><circle cx="7" cy="7" r="5.5" fill="none" stroke="currentColor" stroke-width="1.3"/><path d="M7 4v3.5l2 1.5" fill="none" stroke="currentColor" stroke-width="1.3"/></svg>Operating Hours: 9AM To 5PM Monday - Friday</li>
    </ul>
    <div class="social" aria-label="Registration and social links"><i></i><i></i><i></i><i></i></div>
    <nav class="footer-col" style="left:614px">
      <h4>ACCOMMODATION</h4>
      <a>Supported Independent Living (SIL)</a>
      <a>Specialist Disability Accommodation (SDA)</a>
      <a>Short term Accommodation (Respite)</a>
      <a>Vacancies</a>
    </nav>
    <nav class="footer-col" style="left:884px">
      <h4>WHAT WE DO</h4>
      <a>In Home Care</a>
      <a>Social &amp; Community Services</a>
      <a>Therapeutic Supports</a>
      <a>Support Coordination</a>
      <a>Home Modifications</a>
    </nav>
  </footer>
  <div class="copyright">© Copyright 2021 | Tallowmere Healthcare | All Rights Reserved.</div>
</div>
</body>
</html>
```